Web Design Project - vR Advise

We want to modernise our web page profile. We have an existing web site that we are particularly not proud of (www.vradvise.com.au).
We have started to build a new web site using Plivex and we like the structure of it, but we need it to be professionally designed and implemented.

This current development site can be viewed here: dev.vradvise.com.au

We would like a complete design for the entire website, ready for deployment.

(We still need to finalise the content, as we have just developed new products that we hope to launch in August both on this web site and by a Vendor Forum.)
Updates

Reason: Project must be complete by this friday at the latest.

Target Market(s)

Larger companies where the robustness of their IT infrastructure is critical. Our tools and services provide for monitoring of every device

Industry/Entity Type

Build

Requirements
Must have
• Responsive design for different screen sizes.

BrightDock help desk software integrated with the website.
Currently can be viewed at support.vradvise.com.au
Brightdock only supports custom css.

Nice to have
• Customer experience testimonials in a rotating banner
Chirply and Pagebook links in the footer
We use Avenir as a company font.
Use company colours as in the logo (green and blue)

```html
<!DOCTYPE html>
<html lang="en">
<head>
<meta charset="utf-8">
<title>vR Advise</title>
<link rel="stylesheet" href="https://fonts.googleapis.com/css2?family=Open+Sans:wght@300;400;600;700&family=PT+Sans+Narrow:wght@700&display=swap">
<style>
  :root {
    --canvas-bg: #e6e7e9;
    --page-bg: #ffffff;
    --section-bg: #f7f7f7;
    --brand-green: #6fb52c;
    --button-green: #80b928;
    --button-green-dark: #5f9a17;
    --nav-grey: #7d7d7d;
    --heading-grey: #555555;
    --wordmark: #4a4a4a;
    --white: #ffffff;
    --hero-dark: #2b231d;
    --hero-mid: #5a4634;
    --hero-warm: #7b5c40;
  }
  * { box-sizing: border-box; margin: 0; padding: 0; }
  html, body { width: 1200px; height: 972px; overflow: hidden; }
  body {
    background: var(--canvas-bg);
    font-family: "Open Sans", Arial, sans-serif;
    position: relative;
  }
  a { text-decoration: none; }
  .site {
    position: absolute;
    left: 0; top: 144px;
    width: 1200px; height: 683px;
    background: var(--page-bg);
    overflow: hidden;
  }
  .site-header {
    position: absolute; left: 0; top: 0;
    width: 1200px; height: 78px;
    background: var(--page-bg);
  }
  .brand {
    position: absolute; left: 186px; top: 25px;
    font-size: 21px; font-weight: 600;
    color: var(--wordmark);
  }
  .main-nav {
    position: absolute; top: 36px; left: 0;
    width: 1200px; height: 20px;
  }
  .main-nav a {
    position: absolute;
    font-size: 12px; font-weight: 700;
    letter-spacing: 0.6px;
    color: var(--nav-grey);
  }
  .hero {
    position: absolute; left: 0; top: 78px;
    width: 1200px; height: 429px;
    background: radial-gradient(ellipse at 30% 40%, var(--hero-warm) 0%, var(--hero-mid) 40%, var(--hero-dark) 100%);
    overflow: hidden;
  }
  .hero-photo {
    position: absolute; left: 653px; top: 51px;
    width: 317px; height: 378px;
    background: linear-gradient(160deg, #3a3a3a 0%, #1c1c1c 35%, #c8906c 70%, #a86e4e 100%);
    border-radius: 30px 30px 0 0;
    opacity: 0.9;
  }
  .hero-title {
    position: absolute; left: 174px; top: 86px;
    font-family: "PT Sans Narrow", "Arial Narrow", sans-serif;
    font-weight: 700; font-size: 38px; line-height: 35px;
    color: var(--white);
    text-transform: uppercase;
  }
  .hero-text {
    position: absolute; left: 175px; top: 184px;
    width: 320px;
    font-size: 14px; line-height: 20px;
    color: var(--white);
  }
  .hero-button {
    position: absolute; left: 172px; top: 252px;
    width: 250px; height: 55px;
    padding: 4px;
    background: rgba(20, 20, 20, 0.55);
    border-radius: 4px;
  }
  .hero-button span {
    display: flex; align-items: center; justify-content: center;
    width: 100%; height: 100%;
    background: linear-gradient(var(--button-green), var(--button-green-dark));
    border-radius: 3px;
    font-size: 17px; font-weight: 600;
    color: var(--white);
  }
  .slider-arrow {
    position: absolute; top: 185px;
    width: 54px; height: 54px;
  }
  .slider-arrow.prev { left: 45px; }
  .slider-arrow.next { left: 1100px; }
  .services {
    position: absolute; left: 0; top: 507px;
    width: 1200px; height: 176px;
    background: var(--section-bg);
  }
  .services-title {
    position: absolute; top: 57px; left: 0; width: 1200px;
    text-align: center;
    font-size: 26px; font-weight: 300;
    color: var(--heading-grey);
    letter-spacing: 0.5px;
  }
  .service-icon {
    position: absolute; top: 128px;
    width: 90px; height: 96px;
  }
</style>
</head>
<body>
  <div class="site">
    <header class="site-header">
      <a class="brand" href="#">vR Advise</a>
      <nav class="main-nav">
        <a href="#" style="left:614px">HOME</a>
        <a href="#" style="left:685px">SERVICES</a>
        <a href="#" style="left:773px">PRODUCTS</a>
        <a href="#" style="left:872px">ABOUT US</a>
        <a href="#" style="left:966px">CONTACT</a>
      </nav>
    </header>

    <section class="hero">
      <div class="hero-photo" role="img" aria-label="Photo of a hand holding a smartphone showing a colourful home screen"></div>
      <h1 class="hero-title">Any device, any<br>platorm, anywhere</h1>
      <p class="hero-text">Cross-Domain, performance and services and level monitoring and management.</p>
      <a class="hero-button" href="#"><span>Learn More</span></a>
      <svg class="slider-arrow prev" viewBox="0 0 54 54" aria-label="Previous slide">
        <circle cx="27" cy="27" r="27" fill="rgba(40,40,40,0.7)"/>
        <path d="M30 19 L22 27 L30 35" fill="none" stroke="#fff" stroke-width="3" stroke-linecap="round" stroke-linejoin="round"/>
      </svg>
      <svg class="slider-arrow next" viewBox="0 0 54 54" aria-label="Next slide">
        <circle cx="27" cy="27" r="27" fill="rgba(40,40,40,0.7)"/>
        <path d="M24 19 L32 27 L24 35" fill="none" stroke="#fff" stroke-width="3" stroke-linecap="round" stroke-linejoin="round"/>
      </svg>
    </section>

    <section class="services">
      <h2 class="services-title">vR Advise SERVICES</h2>
      <svg class="service-icon" style="left:255px" viewBox="0 0 90 96" aria-label="Integration service">
        <path d="M45 0 L90 24 L90 72 L45 96 L0 72 L0 24 Z" fill="var(--brand-green)"/>
        <g fill="none" stroke="#fff" stroke-width="4">
          <rect x="38" y="36" width="14" height="14"/>
          <circle cx="33" cy="31" r="5"/><circle cx="57" cy="31" r="5"/>
          <circle cx="33" cy="55" r="5"/><circle cx="57" cy="55" r="5"/>
        </g>
      </svg>
      <svg class="service-icon" style="left:555px" viewBox="0 0 90 96" aria-label="Support service">
        <path d="M45 0 L90 24 L90 72 L45 96 L0 72 L0 24 Z" fill="var(--brand-green)"/>
        <circle cx="45" cy="30" r="5" fill="#fff"/>
        <rect x="40" y="39" width="10" height="22" fill="#fff"/>
      </svg>
      <svg class="service-icon" style="left:854px" viewBox="0 0 90 96" aria-label="Product service">
        <path d="M45 0 L90 24 L90 72 L45 96 L0 72 L0 24 Z" fill="var(--brand-green)"/>
        <path d="M45 22 L64 32 L45 42 L26 32 Z" fill="#fff"/>
        <path d="M26 36 L43 45 L43 64 L26 55 Z M64 36 L47 45 L47 64 L64 55 Z" fill="#fff"/>
      </svg>
    </section>
  </div>
</body>
</html>
```